Need Catering Menu designed - design that we want is attached

Hi,
We need a new catering menu designed for our cafe.
I have attached our coffee menu, we would like it to follow the same kind of layout.
It needs to be A4, and can be double sided.
I have attached a word doc of our catering menu, so this is what needs to be on the catering menu you produce.
Also, our contact details need to be on both sides of the menu:
Visit us instore to discuss catering options, or call 0438 672 914 or email marla@tevrostudio.com.au
I have also attached our new logo which I'd like incorporated into the menu
Target Market(s)
Doctors/Nurses
Hospital staff
University Students
Industry/Entity Type
Catering
Look and feel

```html
<!DOCTYPE html>
<html lang="en">
<head>
<meta charset="utf-8">
<title>Ward Bench Catering Menu</title>
<link href="https://fonts.googleapis.com/css2?family=Josefin+Sans:wght@300;400;600&display=swap" rel="stylesheet">
<style>
  :root {
    --bg: #3b2f2f;
    --cream: #f6eea0;
    --cream-text: #f3e8a6;
    --white: #f4f0e6;
    --dark: #3b2f2f;
  }
  * { box-sizing: border-box; margin: 0; padding: 0; }
  html, body { width: 1200px; height: 848px; overflow: hidden; background: var(--bg); }
  body { position: relative; font-family: "Josefin Sans", sans-serif; color: var(--cream-text); }

  .brand {
    position: absolute; left: 234px; top: 36px; width: 176px; height: 152px;
    background: var(--cream); display: flex; align-items: center; justify-content: center;
  }
  .brand-name {
    font-weight: 400; font-size: 19px; letter-spacing: 2px; color: var(--dark);
    text-align: center; line-height: 1.3;
  }

  .menu-title {
    position: absolute; left: 150px; top: 208px; width: 338px;
    display: flex; align-items: center; gap: 10px;
    font-size: 28px; font-weight: 400; color: var(--white); letter-spacing: 0.5px;
  }
  .menu-title .rule {
    flex: 1; height: 7px; border-top: 2px solid var(--white); border-bottom: 2px solid var(--white);
  }

  .section { position: absolute; border: 2px solid var(--cream); }
  .section-title {
    position: absolute; background: var(--bg); border: 2px solid var(--cream);
    display: flex; flex-direction: column; align-items: center; justify-content: center;
    font-weight: 400; color: var(--cream); letter-spacing: 6px; line-height: 1.1;
  }

  .breakfast { left: 65px; top: 292px; width: 508px; height: 456px; }
  .breakfast-title { left: 143px; top: 261px; width: 356px; height: 64px; font-size: 33px; }

  .tea { left: 630px; top: 60px; width: 536px; height: 446px; }
  .tea-title { left: 691px; top: 29px; width: 391px; height: 103px; font-size: 33px; }

  .hot { left: 630px; top: 573px; width: 508px; height: 238px; }
  .hot-title { left: 708px; top: 541px; width: 356px; height: 64px; font-size: 33px; }

  .items { position: absolute; list-style: none; font-size: 19px; font-weight: 400; }
  .items li { display: flex; align-items: baseline; height: 27.4px; white-space: nowrap; }
  .items .leader { flex: 1; border-bottom: 2px dotted var(--cream-text); margin: 0 2px; transform: translateY(-3px); }

  .breakfast-items { left: 121px; top: 361px; width: 398px; }
  .tea-items { left: 673px; top: 154px; width: 427px; }
  .hot-items { left: 673px; top: 628px; width: 427px; }

  .notes { position: absolute; left: 673px; top: 419px; width: 440px; font-size: 14px; line-height: 1.45; color: var(--cream-text); }

  .contact {
    position: absolute; left: 70px; top: 757px; width: 500px; text-align: center;
    font-size: 17px; line-height: 1.3; color: var(--white);
  }
</style>
</head>
<body>
  <div class="brand"><p class="brand-name">WARD<br>BENCH</p></div>

  <h1 class="menu-title"><span class="rule"></span>CATERING MENU<span class="rule"></span></h1>

  <div class="section breakfast"></div>
  <h2 class="section-title breakfast-title">BREAKFAST</h2>
  <ul class="items breakfast-items">
    <li>Fruit Platter<span class="leader"></span>$15</li>
    <li>Bacon Egg and Cheese Roll<span class="leader"></span>$6.5</li>
    <li>Vegetarian Brekky Wrap<span class="leader"></span>$6.5</li>
    <li>Ham and Cheese Croissant<span class="leader"></span>$6</li>
    <li>Cheese and Tomato Croissant<span class="leader"></span>$5.5</li>
    <li>Ham and Cheese French Toast<span class="leader"></span>$6.5</li>
    <li>Assorted Yoghurts<span class="leader"></span>$5.5</li>
    <li>Bircher Muesli<span class="leader"></span>$5.5</li>
    <li>Chia Pudding<span class="leader"></span>$5.5</li>
    <li>Granola and Yoghurt<span class="leader"></span>$5.5</li>
    <li>Muffin<span class="leader"></span>$4.5</li>
    <li>Mini Muffin<span class="leader"></span>$2.5</li>
    <li>Juice<span class="leader"></span>$8</li>
  </ul>

  <p class="contact">Visit us instore to discuss catering options, or<br>call: 0438 672 914 email: marla@tevrostudio.com.au</p>

  <div class="section tea"></div>
  <h2 class="section-title tea-title"><span>MORNING &amp;</span><span>AFTERNOON TEA</span></h2>
  <ul class="items tea-items">
    <li>Fruit Platter<span class="leader"></span>$15</li>
    <li>Muffin<span class="leader"></span>$4.5</li>
    <li>Mini Muffin<span class="leader"></span>$2.5</li>
    <li>Assorted Slices<span class="leader"></span>$4</li>
    <li>Assorted Cookies from<span class="leader"></span>$3</li>
    <li>Assorted Yoghurts<span class="leader"></span>$5.5</li>
    <li>Chia Pudding<span class="leader"></span>$5.5</li>
    <li>Banana Bread<span class="leader"></span>$4.5</li>
    <li>Juice<span class="leader"></span>$8</li>
  </ul>
  <p class="notes">*Cups/Plates/Serviettes can be provided at a charge of $1 per person<br>*Barista made coffee available</p>

  <div class="section hot"></div>
  <h2 class="section-title hot-title">HOT FOOD</h2>
  <ul class="items hot-items">
    <li>Assorted Pies<span class="leader"></span>$5.0</li>
    <li>Large tray hot chips<span class="leader"></span>$15</li>
    <li>Small tray hot chips<span class="leader"></span>$9</li>
    <li>Mini samosa<span class="leader"></span>$3</li>
    <li>Vegetarian spring rolls<span class="leader"></span>$3</li>
    <li>Party pies<span class="leader"></span>$3</li>
  </ul>
</body>
</html>
```